Torvel, Inc. new buisness cards - brand guide included

We need new business cards. SLEAK SIMPLE FINANCE. They must include a place for NAME, TITLE, CELL, OFFICE PHONE, EMAIL. they also must include our services across the bottom. AIR, OCEAN, FTL, LTL, EXPRESS. for reference this will be being handed to some of the most prestigious shipping companies in a america.

Target Market(s)

Finance and corporate

Contact Information for Business Card

We need new business cards. SLEAK SIMPLE FINANCE. They must include a place for NAME, TITLE, CELL, OFFICE PHONE, EMAIL. they also must include our services across the bottom. AIR, OCEAN, FTL, LTL, EXPRESS.

Requirements
Must have
• We need new business cards. SLEAK SIMPLE FINANCE. They must include a place for NAME, TITLE, CELL, OFFICE PHONE, EMAIL. they also must include our services across the bottom. AIR, OCEAN, FTL, LTL, EXPRESS.
Nice to have
• USE THE COLORS AND LOGO IN THE BRAND GUIDE :)

```html
<!DOCTYPE html>
<html lang="en">
<head>
<meta charset="utf-8">
<title>Torvel, Inc. Business Cards</title>
<link rel="stylesheet" href="https://fonts.googleapis.com/css2?family=Poppins:wght@400;500;600&display=swap">
<style>
  :root {
    --backdrop: #cdbfa9;
    --card: #333333;
    --gold: #c4b493;
    --band: #c2b396;
    --ink: #ffffff;
    --rule: #b9aa8b;
  }
  * { margin: 0; padding: 0; box-sizing: border-box; }
  html, body {
    width: 916px; height: 1200px; overflow: hidden;
    background: var(--backdrop);
    font-family: "Poppins", sans-serif;
  }
  .canvas { position: relative; width: 916px; height: 1200px; }
  .card {
    position: absolute; left: 71px; width: 777px; height: 464px;
    background: var(--card); border-radius: 22px; overflow: hidden;
    box-shadow: 0 8px 18px rgba(0,0,0,.35);
  }
  .card-front { top: 107px; }
  .card-back { top: 640px; }

  .wordmark {
    position: absolute; color: var(--gold); font-weight: 500;
    letter-spacing: .08em; line-height: 1; white-space: nowrap;
    transform: translate(-50%, -50%);
  }
  .card-front .wordmark { left: 388px; top: 232px; font-size: 92px; }
  .card-back .wordmark { left: 585px; top: 129px; font-size: 50px; }

  .holder-name {
    position: absolute; left: 41px; top: 230px;
    color: var(--gold); font-size: 26px; font-weight: 600; line-height: 1;
  }
  .holder-title {
    position: absolute; left: 41px; top: 261px;
    color: var(--ink); font-size: 16px; line-height: 1;
  }
  .rule {
    position: absolute; left: 41px; top: 284px; width: 783px; max-width: 712px;
    height: 2px; background: var(--rule);
  }
  .contact-list {
    position: absolute; left: 41px; top: 298px; list-style: none;
  }
  .contact-list li {
    display: flex; align-items: center; gap: 9px;
    height: 25px; color: var(--ink); font-size: 16.5px;
  }
  .contact-list svg { width: 20px; height: 20px; flex: none; }
  .address {
    position: absolute; left: 510px; top: 340px;
    color: var(--ink); font-size: 16.5px; line-height: 21px; font-style: normal;
  }
  .services {
    position: absolute; left: 0; top: 410px; width: 100%; height: 38px;
    background: var(--band); display: flex; justify-content: center; align-items: center;
    gap: 12px; list-style: none; color: var(--ink); font-size: 15.5px; letter-spacing: .02em;
  }
  .services li::before { content: "\2022"; margin-right: 8px; }
</style>
</head>
<body>
<main class="canvas">
  <section class="card card-front" aria-label="Card front">
    <div class="wordmark">TORVEL</div>
  </section>

  <section class="card card-back" aria-label="Card back">
    <div class="wordmark">TORVEL</div>
    <h1 class="holder-name">Daniel Reyes</h1>
    <p class="holder-title">Head contractor</p>
    <div class="rule"></div>
    <ul class="contact-list">
      <li>
        <svg viewBox="0 0 20 20" aria-hidden="true"><circle cx="10" cy="10" r="10" fill="var(--gold)"/><path d="M6 8.5c0-1.5 1.8-2.5 4-2.5s4 1 4 2.5v1h-2.2v-1h-3.6v1H6z M7 10.5h6l1 3.5H6z" fill="var(--card)"/></svg>
        <span>555-014-2290</span>
      </li>
      <li>
        <svg viewBox="0 0 20 20" aria-hidden="true"><circle cx="10" cy="10" r="10" fill="var(--gold)"/><rect x="7" y="4.5" width="6" height="11" rx="1" fill="var(--card)"/><rect x="8" y="6" width="4" height="7" fill="var(--gold)"/></svg>
        <span>555-014-2290</span>
      </li>
      <li>
        <svg viewBox="0 0 20 20" aria-hidden="true"><circle cx="10" cy="10" r="10" fill="var(--gold)"/><rect x="5" y="6.5" width="10" height="7" fill="var(--card)"/><path d="M5 6.5l5 4 5-4" fill="none" stroke="var(--gold)" stroke-width="1"/></svg>
        <span>accounting@torvelinc.com</span>
      </li>
      <li>
        <svg viewBox="0 0 20 20" aria-hidden="true"><circle cx="10" cy="10" r="10" fill="var(--gold)"/><circle cx="10" cy="10" r="5" fill="none" stroke="var(--card)" stroke-width="1.4"/><path d="M5 10h10M10 5c-2 2.5-2 7.5 0 10M10 5c2 2.5 2 7.5 0 10" fill="none" stroke="var(--card)" stroke-width="1"/></svg>
        <span>www.torvelinc.com</span>
      </li>
    </ul>
    <address class="address">4120 Harbor Loop Ste 210<br>Alder Bay, WA 98041</address>
    <ul class="services">
      <li>AIR</li><li>OCEAN</li><li>FTL</li><li>LTL</li><li>EXPRESS</li>
    </ul>
  </section>
</main>
</body>
</html>
```